From Portrait to Landscape

Take a PPT document made of 54 slide of graphs, images and text and change the orientation of each one of the 54 slides from the existing Portrait layout to the Landscape one.
All the graphics and texts (including text formatting, commas, bullet points etc.) must be kept the same but spaces are reorganized in the new Landscape orientation favoring the size of the graphs (possibily reducing the text areas).
Please, find attached the first 10 pages of the PPT document (for now, in PDF format) and a couple of sample pages of the PPT.x\

Target Market(s)

Readers of the Report (ecommerce players in Italy)

Requirements
Must have
• Graphics should be larger in the Landscape orientation than they are now in the Poirtrait one

```html
<!DOCTYPE html>
<html lang="it">
<head>
<meta charset="utf-8">
<title>Web Retail – Impaginazione orizzontale</title>
<link href="https://fonts.googleapis.com/css2?family=Open+Sans:wght@400;600;700&family=PT+Sans+Narrow:wght@400;700&display=swap" rel="stylesheet">
<style>
  :root{
    --page:#e6e6e6;
    --paper:#ffffff;
    --navy:#1f2d5a;
    --olive:#8c9a2b;
    --olive-light:#c7d07a;
    --olive-pale:#e7ecc4;
    --section-green:#7f9b3b;
    --orange:#f1922b;
    --orange-light:#f8c27c;
    --yellow:#f4c430;
    --teal:#2ba3b6;
    --red:#d9483b;
    --blue:#3a78b8;
    --purple:#7b5aa6;
    --ink:#3a3a3a;
    --ink-soft:#777;
    --rule:#cfcfcf;
  }
  *{box-sizing:border-box;margin:0;padding:0}
  html,body{width:720px;height:1200px;overflow:hidden;background:var(--page)}
  body{font-family:"Open Sans",Arial,sans-serif;color:var(--ink)}
  .deck{
    display:grid;grid-template-columns:330px 330px;grid-template-rows:repeat(5,214px);
    gap:20px;padding:25px 20px;width:720px;height:1200px;
  }
  .slide{position:relative;background:var(--paper);overflow:hidden;box-shadow:0 1px 3px rgba(0,0,0,.18)}
  .slide-head{position:absolute;left:14px;top:10px;right:14px}
  .slide-title{font-family:"PT Sans Narrow",Arial,sans-serif;font-weight:700;font-size:15px;color:var(--olive);text-transform:uppercase;letter-spacing:.2px;line-height:1.1}
  .slide-sub{font-size:7.5px;color:var(--ink-soft);margin-top:1px}
  .slide-foot{position:absolute;left:0;right:0;bottom:0;height:7px;background:var(--olive)}
  .small{font-size:5px;line-height:1.45;color:var(--ink-soft)}

  /* cover */
  .cover{background:var(--navy)}
  .cover-art{position:absolute;left:90px;top:12px;width:190px;height:190px;border-radius:50%;
    background:radial-gradient(circle,rgba(255,255,255,0) 58%,rgba(244,196,48,.55) 66%,rgba(43,163,182,.55) 78%,rgba(31,45,90,0) 92%)}
  .cover-disc{position:absolute;left:120px;top:42px;width:130px;height:130px;border-radius:50%;background:var(--paper);
    display:flex;flex-direction:column;align-items:center;justify-content:center;text-align:center}
  .cover-date{font-size:6px;color:var(--ink-soft);margin-bottom:6px}
  .cover-title{font-family:"PT Sans Narrow",Arial,sans-serif;font-size:22px;font-weight:700;color:var(--navy);letter-spacing:.5px}
  .cover-tag{font-size:6px;color:var(--ink-soft);margin-top:4px;width:100px}

  /* index */
  .index-title{position:absolute;left:22px;top:18px;font-family:"PT Sans Narrow",Arial,sans-serif;font-weight:700;font-size:15px;color:var(--orange);text-transform:uppercase}
  .index-list{position:absolute;left:22px;right:22px;top:46px;list-style:none}
  .index-list li{display:flex;justify-content:space-between;font-size:7.5px;padding:3.2px 0;border-bottom:1px solid #eee}
  .index-list .pg{color:var(--ink-soft)}

  /* consortium */
  .org-title{font-family:"PT Sans Narrow",Arial,sans-serif;font-weight:700;font-size:15px;color:var(--teal)}
  .org-sub{font-size:7.5px;color:var(--ink-soft)}
  .org-name{position:absolute;left:14px;top:50px;display:flex;align-items:center;gap:5px;font-size:14px;font-weight:700;color:var(--teal)}
  .org-name .dot{width:10px;height:10px;border-radius:50%;background:var(--teal)}
  .org-text{position:absolute;left:14px;right:14px;top:72px}
  .org-text p{margin-bottom:3px}
  .org-foot{position:absolute;left:0;right:0;bottom:0;height:7px;background:var(--teal)}

  /* section */
  .section{background:var(--section-green)}
  .section-title{position:absolute;left:0;right:0;top:0;padding:12px 14px;border-bottom:2px solid rgba(255,255,255,.85);
    font-family:"PT Sans Narrow",Arial,sans-serif;font-weight:700;font-size:15px;color:#fff;text-transform:uppercase}
  .section-art{position:absolute;left:70px;top:50px;width:200px;height:150px;border-radius:6px;
    background:linear-gradient(135deg,rgba(255,255,255,.22),rgba(255,255,255,.06))}

  /* table */
  .data-table{position:absolute;left:14px;right:14px;top:44px;border-collapse:collapse;font-size:6px}
  .data-table th{background:var(--olive);color:#fff;font-weight:600;text-align:left;padding:2px 4px}
  .data-table td{padding:1.9px 4px;border-bottom:1px solid #eee}
  .data-table td.num{text-align:right}
  .data-table tr:nth-child(even) td{background:#f6f7ee}

  /* tiles */
  .tiles{position:absolute;left:14px;right:14px;top:44px;display:grid;grid-template-columns:repeat(3,1fr);grid-auto-rows:36px;gap:3px}
  .tile{color:#fff;padding:3px 5px;font-size:5px;line-height:1.35}
  .tile b{display:block;font-size:9px;font-family:"PT Sans Narrow",Arial,sans-serif}
  .t-orange{background:var(--orange)} .t-green{background:var(--olive)} .t-blue{background:var(--blue)}
  .t-red{background:var(--red)} .t-teal{background:var(--teal)} .t-purple{background:var(--purple)}

  .chart{position:absolute}
  .side-text{position:absolute;right:14px;width:92px}
  .side-text h4{font-size:6.5px;color:var(--olive);margin-bottom:2px}
</style>
</head>
<body>
<main class="deck">

  <!-- 1 cover -->
  <section class="slide cover">
    <div class="cover-art" role="img" aria-label="Corona di piccole icone colorate dello shopping online attorno al titolo"></div>
    <div class="cover-disc">
      <div class="cover-date">Aprile 2014</div>
      <div class="cover-title">Web Retail</div>
      <div class="cover-tag">Gli acquisti digitali degli italiani</div>
    </div>
  </section>

  <!-- 2 index -->
  <section class="slide">
    <h2 class="index-title">Indice del documento</h2>
    <ul class="index-list">
      <li style="color:var(--olive)"><span>Lo sviluppo dell'ecommerce in Italia</span><span class="pg">04</span></li>
      <li style="color:var(--orange)"><span>Il percorso verso l'acquisto</span><span class="pg">12</span></li>
      <li style="color:var(--red)"><span>I fattori chiave di scelta</span><span class="pg">20</span></li>
      <li style="color:var(--teal)"><span>Modalità di pagamento</span><span class="pg">26</span></li>
      <li style="color:var(--blue)"><span>Consegna, ritiro e restituzione</span><span class="pg">32</span></li>
      <li style="color:var(--purple)"><span>Servizi e canali di contatto</span><span class="pg">38</span></li>
      <li style="color:var(--section-green)"><span>Le categorie di prodotto</span><span class="pg">44</span></li>
      <li style="color:var(--yellow)"><span>Le soluzioni digitali nei negozi</span><span class="pg">48</span></li>
      <li style="color:var(--ink-soft)"><span>Nota metodologica</span><span class="pg">52</span></li>
    </ul>
  </section>

  <!-- 3 consortium -->
  <section class="slide">
    <div class="slide-head">
      <div class="org-title">DIGICOMM</div>
      <div class="org-sub">Il consorzio del commercio digitale italiano</div>
    </div>
    <div class="org-name"><span class="dot"></span>Digicomm</div>
    <div class="org-text small">
      <p>Digicomm riunisce aziende italiane e internazionali che operano nel commercio elettronico, nei servizi di pagamento, nella logistica e nella comunicazione digitale, con l'obiettivo di favorire la crescita del mercato online.</p>
      <p>Il consorzio promuove ricerche, osservatori e momenti di confronto tra operatori, istituzioni e consumatori, e rilascia un marchio di qualità ai siti che rispettano un codice di condotta condiviso.</p>
      <p>Tra le attività principali: formazione, analisi dei dati di mercato, tutela degli acquirenti, diffusione di buone pratiche e sostegno all'internazionalizzazione delle imprese italiane.</p>
    </div>
    <div class="org-foot"></div>
  </section>

  <!-- 4 section -->
  <section class="slide section">
    <h2 class="section-title">Lo sviluppo dell'ecommerce in Italia</h2>
    <div class="section-art" role="img" aria-label="Disegno al tratto bianco di una figura che porta una grande fetta di torta"></div>
  </section>

  <!-- 5 table -->
  <section class="slide">
    <div class="slide-head">
      <h2 class="slide-title">L'ecommerce in Italia</h2>
      <div class="slide-sub">Dimensioni e trend</div>
    </div>
    <table class="data-table">
      <tr><th>Indicatore</th><th>2013</th><th>Trend</th></tr>
      <tr><td>Utenti internet (milioni)</td><td class="num">29,1</td><td class="num">+4%</td></tr>
      <tr><td>Acquirenti online (milioni)</td><td class="num">16,3</td><td class="num">+11%</td></tr>
      <tr><td>Acquirenti abituali (milioni)</td><td class="num">11,6</td><td class="num">+14%</td></tr>
      <tr><td>Valore acquisti (mld €)</td><td class="num">11,3</td><td class="num">+17%</td></tr>
      <tr><td>Spesa media annua (€)</td><td class="num">693</td><td class="num">+5%</td></tr>
      <tr><td>Acquisti da mobile (%)</td><td class="num">14</td><td class="num">+6 pt</td></tr>
      <tr><td>Siti di vendita attivi</td><td class="num">17.200</td><td class="num">+9%</td></tr>
      <tr><td>Pagamenti con carta (%)</td><td class="num">58</td><td class="num">-2 pt</td></tr>
      <tr><td>Consegne a domicilio (%)</td><td class="num">81</td><td class="num">=</td></tr>
      <tr><td>Quota sul retail totale (%)</td><td class="num">3,5</td><td class="num">+0,6 pt</td></tr>
    </table>
    <div class="slide-foot"></div>
  </section>

  <!-- 6 tiles -->
  <section class="slide">
    <div class="slide-head">
      <h2 class="slide-title">L'ecommerce in Italia</h2>
      <div class="slide-sub">Risultati indicatori del fenomeno</div>
    </div>
    <div class="tiles">
      <div class="tile t-orange"><b>16,3 mln</b>acquirenti online nel corso dell'anno</div>
      <div class="tile t-green"><b>11,3 mld €</b>valore complessivo degli acquisti</div>
      <div class="tile t-blue"><b>+17%</b>crescita rispetto all'anno precedente</div>
      <div class="tile t-red"><b>693 €</b>spesa media per acquirente</div>
      <div class="tile t-teal"><b>14%</b>acquisti completati da mobile</div>
      <div class="tile t-purple"><b>58%</b>pagamenti con carta di credito</div>
      <div class="tile t-green"><b>81%</b>consegne effettuate a domicilio</div>
      <div class="tile t-orange"><b>3,5%</b>quota sul commercio al dettaglio</div>
      <div class="tile t-blue"><b>17.200</b>siti di vendita attivi nel paese</div>
      <div class="tile t-teal"><b>6,8</b>acquisti medi per persona</div>
      <div class="tile t-red"><b>42%</b>usa confronto prezzi prima di comprare</div>
      <div class="tile t-purple"><b>27%</b>ha acquistato da siti esteri</div>
    </div>
    <div class="slide-foot"></div>
  </section>

  <!-- 7 bars + circle -->
  <section class="slide">
    <div class="slide-head">
      <h2 class="slide-title">Le dimensioni del fenomeno</h2>
      <div class="slide-sub">La diffusione dell'esperienza di acquisto online in Italia</div>
    </div>
    <svg class="chart" style="left:14px;top:46px" width="302" height="150" viewBox="0 0 302 150">
      <line x1="0" y1="140" x2="300" y2="140" stroke="var(--rule)"/>
      <g fill="var(--olive-light)">
        <rect x="6" y="128" width="9" height="12"/><rect x="19" y="124" width="9" height="16"/><rect x="32" y="120" width="9" height="20"/>
        <rect x="45" y="115" width="9" height="25"/><rect x="58" y="110" width="9" height="30"/><rect x="71" y="104" width="9" height="36"/>
        <rect x="84" y="98" width="9" height="42"/><rect x="97" y="92" width="9" height="48"/><rect x="110" y="86" width="9" height="54"/>
        <rect x="123" y="80" width="9" height="60"/><rect x="136" y="73" width="9" height="67"/><rect x="149" y="66" width="9" height="74"/>
        <rect x="162" y="58" width="9" height="82"/><rect x="175" y="50" width="9" height="90"/><rect x="188" y="42" width="9" height="98"/>
      </g>
      <g fill="var(--olive)">
        <rect x="6" y="134" width="9" height="6"/><rect x="19" y="132" width="9" height="8"/><rect x="32" y="130" width="9" height="10"/>
        <rect x="45" y="127" width="9" height="13"/><rect x="58" y="124" width="9" height="16"/><rect x="71" y="120" width="9" height="20"/>
        <rect x="84" y="116" width="9" height="24"/><rect x="97" y="112" width="9" height="28"/><rect x="110" y="107" width="9" height="33"/>
        <rect x="123" y="102" width="9" height="38"/><rect x="136" y="97" width="9" height="43"/><rect x="149" y="91" width="9" height="49"/>
        <rect x="162" y="85" width="9" height="55"/><rect x="175" y="78" width="9" height="62"/><rect x="188" y="70" width="9" height="70"/>
      </g>
      <circle cx="252" cy="70" r="46" fill="var(--olive)" opacity=".85"/>
      <text x="252" y="66" text-anchor="middle" font-size="15" font-weight="700" fill="#fff" font-family="PT Sans Narrow, sans-serif">16,3 mln</text>
      <text x="252" y="78" text-anchor="middle" font-size="6" fill="#fff">acquirenti online</text>
    </svg>
    <div class="slide-foot"></div>
  </section>

  <!-- 8 bars + pie -->
  <section class="slide">
    <div class="slide-head">
      <h2 class="slide-title">Le dimensioni del fenomeno</h2>
      <div class="slide-sub">Il numero di atti di acquisto online</div>
    </div>
    <svg class="chart" style="left:14px;top:46px" width="190" height="150" viewBox="0 0 190 150">
      <line x1="0" y1="140" x2="188" y2="140" stroke="var(--rule)"/>
      <g fill="var(--olive)">
        <rect x="6" y="126" width="10" height="14"/><rect x="21" y="121" width="10" height="19"/><rect x="36" y="115" width="10" height="25"/>
        <rect x="51" y="108" width="10" height="32"/><rect x="66" y="100" width="10" height="40"/><rect x="81" y="92" width="10" height="48"/>
        <rect x="96" y="83" width="10" height="57"/><rect x="111" y="73" width="10" height="67"/><rect x="126" y="62" width="10" height="78"/>
        <rect x="141" y="50" width="10" height="90"/><rect x="156" y="37" width="10" height="103"/><rect x="171" y="22" width="10" height="118"/>
      </g>
    </svg>
    <svg class="chart" style="left:214px;top:56px" width="102" height="102" viewBox="0 0 102 102">
      <circle cx="51" cy="51" r="48" fill="var(--olive-pale)"/>
      <path d="M51 51 L51 3 A48 48 0 0 1 97.6 62.4 Z" fill="var(--olive)"/>
      <path d="M51 51 L97.6 62.4 A48 48 0 0 1 66 96.6 Z" fill="var(--olive-light)"/>
    </svg>
    <div class="side-text small" style="top:164px;width:100px">
      <h4>Acquisti per frequenza</h4>Abituali 60% · Occasionali 25% · Nuovi 15%
    </div>
    <div class="slide-foot"></div>
  </section>

  <!-- 9 orange bars + text -->
  <section class="slide">
    <div class="slide-head">
      <h2 class="slide-title">Il valore degli acquisti online</h2>
      <div class="slide-sub">Il valore degli acquisti online sviluppato dagli italiani</div>
    </div>
    <svg class="chart" style="left:14px;top:46px" width="200" height="150" viewBox="0 0 200 150">
      <line x1="0" y1="140" x2="198" y2="140" stroke="var(--rule)"/>
      <g fill="var(--orange)">
        <rect x="6" y="128" width="11" height="12"/><rect x="22" y="122" width="11" height="18"/><rect x="38" y="115" width="11" height="25"/>
        <rect x="54" y="107" width="11" height="33"/><rect x="70" y="98" width="11" height="42"/><rect x="86" y="88" width="11" height="52"/>
        <rect x="102" y="77" width="11" height="63"/><rect x="118" y="66" width="11" height="74"/><rect x="134" y="54" width="11" height="86"/>
        <rect x="150" y="41" width="11" height="99"/><rect x="166" y="27" width="11" height="113"/><rect x="182" y="12" width="11" height="128"/>
      </g>
    </svg>
    <div class="side-text small" style="top:52px">
      <h4 style="color:var(--orange)">11,3 miliardi di euro</h4>
      <p>Il valore degli acquisti online cresce in modo costante e supera gli undici miliardi annui, trainato da turismo, elettronica e abbigliamento.</p>
      <p style="margin-top:4px">La spesa media per acquirente aumenta insieme alla frequenza d'acquisto, segno di una crescente fiducia nel canale digitale.</p>
    </div>
    <div class="slide-foot"></div>
  </section>

  <!-- 10 orange bars + yellow circle -->
  <section class="slide">
    <div class="slide-head">
      <h2 class="slide-title">Valore e quota degli acquisti online</h2>
      <div class="slide-sub">Contributo dell'online ai valori complessivi del retail</div>
    </div>
    <svg class="chart" style="left:14px;top:46px" width="302" height="150" viewBox="0 0 302 150">
      <line x1="0" y1="140" x2="300" y2="140" stroke="var(--rule)"/>
      <g fill="var(--orange)">
        <rect x="6" y="126" width="12" height="14"/><rect x="24" y="120" width="12" height="20"/><rect x="42" y="113" width="12" height="27"/>
        <rect x="60" y="105" width="12" height="35"/><rect x="78" y="96" width="12" height="44"/><rect x="96" y="86" width="12" height="54"/>
        <rect x="114" y="75" width="12" height="65"/><rect x="132" y="63" width="12" height="77"/><rect x="150" y="50" width="12" height="90"/>
        <rect x="168" y="36" width="12" height="104"/>
      </g>
      <g fill="var(--orange-light)">
        <rect x="6" y="134" width="12" height="6"/><rect x="24" y="132" width="12" height="8"/><rect x="42" y="129" width="12" height="11"/>
        <rect x="60" y="126" width="12" height="14"/><rect x="78" y="122" width="12" height="18"/><rect x="96" y="118" width="12" height="22"/>
        <rect x="114" y="113" width="12" height="27"/><rect x="132" y="108" width="12" height="32"/><rect x="150" y="102" width="12" height="38"/>
        <rect x="168" y="96" width="12" height="44"/>
      </g>
      <circle cx="250" cy="88" r="44" fill="var(--yellow)"/>
      <text x="250" y="78" text-anchor="middle" font-size="6" fill="var(--ink)">I consumi delle famiglie</text>
      <text x="250" y="96" text-anchor="middle" font-size="15" font-weight="700" fill="var(--ink)" font-family="PT Sans Narrow, sans-serif">3,5%</text>
      <text x="250" y="106" text-anchor="middle" font-size="6" fill="var(--ink)">quota dell'online</text>
    </svg>
    <div class="slide-foot"></div>
  </section>

</main>
</body>
</html>
```